Stonefield Partners Business Card Design

We are looking for a new business card design, we are not happy with our current design. We are a boutique management consulting firm and our clients are typically fortune 500 companies.

I have attached the current front and back that we have as well as a version of our logo that can be used. I am trying to get a higher resolution version of the logo file to upload to the project.

Target Market(s)

Fortune 500 companies are our primary client base. Financial services, life sciences, pharmaceuticals and telecom companies are

Industry/Entity Type

Management Consulting

Contact Information for Business Card

We are trying to communicate a high degree of professionalism, a somewhat minimalist perhaps with some air of whimsy (without overdoing it). Attached is the current design, front and back as well as logos. I like the current back of the card and assume we will keep the phrase the same.

From a color palette perspective, I prefer to stay with a gray scale as they are today.

Font styles to use
Sans Serif

Colors
1b1b1b
474747
ffffff

Requirements
Must have
• Two sided business card design. File format should be something that can be used outside of Photoshop like MS Publisher so that they can be edited with personal information.
• Font should be calibri or something very similar and should be available within MS Office
Should not have
• No other logos or graphics outside of the logo provided.

```html
<!DOCTYPE html>
<html lang="en">
<head>
<meta charset="utf-8">
<title>Stonefield Partners Business Card</title>
<link rel="stylesheet" href="https://fonts.googleapis.com/css2?family=Arimo:ital,wght@0,400;0,700;1,700&display=swap">
<style>
  :root {
    --card-black: #000000;
    --ink-white: #ffffff;
    --backdrop: #d4d4d4;
    --shadow: rgba(0,0,0,0.18);
  }
  * { margin: 0; padding: 0; box-sizing: border-box; }
  html, body {
    width: 1200px; height: 2335px; overflow: hidden;
    background: var(--backdrop);
    font-family: "Arimo", Arial, sans-serif;
    color: var(--ink-white);
  }
  .sheet { position: relative; width: 1200px; height: 2335px; }
  .card {
    position: absolute; left: 100px; width: 1000px; height: 571px;
    background: var(--card-black); overflow: hidden;
    box-shadow: 0 6px 20px var(--shadow);
  }
  .card--front { top: 566px; }
  .card--back { top: 1197px; }

  .brand {
    position: absolute; right: 60px; top: 42px;
    display: flex; align-items: center; gap: 22px;
  }
  .brand__dot { width: 70px; height: 70px; border-radius: 50%; background: var(--ink-white); }
  .brand__name { font-size: 122px; font-weight: 400; line-height: 1; letter-spacing: -1px; }
  .brand__tm { position: absolute; right: -30px; top: 4px; font-size: 20px; }

  .company {
    position: absolute; right: 38px; top: 190px; text-align: right;
    font-size: 24px; line-height: 1.45;
  }
  .company__name { font-weight: 700; }

  .person { position: absolute; left: 37px; top: 385px; font-size: 24px; line-height: 1.45; }
  .person__name { font-size: 33px; font-weight: 700; letter-spacing: 0.5px; margin-bottom: 10px; }

  .tagline {
    position: absolute; left: 37px; top: 258px;
    font-size: 38px; font-weight: 700; font-style: italic; line-height: 1.4;
  }
  .website { position: absolute; left: 37px; top: 500px; font-size: 26px; }
  .accent-circle { position: absolute; right: -120px; top: 60px; width: 460px; height: 460px; }
</style>
</head>
<body>
<main class="sheet">
  <section class="card card--front" aria-label="Business card front">
    <div class="brand">
      <span class="brand__dot"></span>
      <span class="brand__name">Stonefield</span>
      <span class="brand__tm">™</span>
    </div>
    <div class="company">
      <p class="company__name">Stonefield Partners, Inc. &nbsp;/&nbsp; Headquarters</p>
      <p class="company__address">218 Orchard Lane Suite 40, Cedar Harbor, WA 98021</p>
    </div>
    <div class="person">
      <p class="person__name">MAREN HOLT</p>
      <p class="person__role">Managing Director &nbsp;/&nbsp; Los Angeles Office</p>
      <p class="person__phone">555.014.2207</p>
      <p class="person__email">mholt@stonefieldpartners.com</p>
    </div>
  </section>

  <section class="card card--back" aria-label="Business card back">
    <svg class="accent-circle" viewBox="0 0 460 460" aria-hidden="true">
      <circle cx="230" cy="230" r="230" fill="#ffffff"/>
    </svg>
    <p class="tagline">The preferred choice<br>for leadership’s top prioroties</p>
    <p class="website">www.stonefieldpartners.com</p>
  </section>
</main>
</body>
</html>
```